Wordpress design for my private practice website - Psychotherapist

I would like a simple, clean, and elegant design for my private practice website. I work with both adults and children so I'd like it to appeal to both. However, since parents make the choice as to where to send their child for therapy, I want it to appeal to adults more. I would like the pictures on the site to have a calming effect - maybe using sand and water and rocks. I am attaching files with my company logo. I would also like my name incorporated into the header - Rosalind Vantreece, LCSW, Registered Play Therapist. I've also uploaded a picture of myself for my About Page.

I like the design of these 2 website and want something similar:
www.drmaribelostrand.com
www.harrowgate-lisk.com

I would like a home page that highlights a calming graphic across the entire top of the page as well as my practice logo and my name.

I'd like a link to social media sites on the top of the homepage - facebook, pinterest.

I want a simple bar across the top with the following tabs:
Home
About Me (subtabs Who I Am, Specialties and Approach)
Counseling Services (subtabs Individual Counseling, Play Therapy, Sandplay Therapy,)
Fees
FAQs
Contact Me (would love this to be a fill in the blank contact form that sends info to my email address - should include name, phone number, email and a comment box for more information requested)
Blog (this will link with another wordpress blog)

Target Market(s)

Parents of children under age 12 with behavioral problems or are dealing with the breakup of their family through divorce - looking for someone to work with their young child. I also work with Adults that are overwhelmed and worried - often women that have many life stressors and are feeling burnt out on life and meeting everyone's needs. Families going through some type of trauma, including divorce or grief work. I also work with individuals going through a transition of religious beliefs - often exiting the religion of their youth and undergoing a crisis of faith at midlife.

Industry/Entity Type

Mental Health

Contact Information for Business Card

Rosalind Vantreece, LCSW
Registered Play Therapist
4815 Bellhaven Court
Idaho Falls, Idaho 83404
(208)555-7162
www.stillbrookwellness.com

On the opposite side, I'd like an appointment reminder area - with the following text:

Your next appointment is
_____/______/______ at ______am/pm
Please give 24 hrs notice if you need to cancel your appointment.

Coding

Coded - Design and coding required

Number of Pages Required

5+ page

Font styles to use
Sans Serif

Colors
33a6d7
9bcb3c
0355a3

Requirements
Must have
• I'd like it to be a wordpress site. I'm such a newby at web design - but I need to be able to add content and manage the site myself once it is up and running.
Nice to have
• I like the design of these 2 websites and want something similar:
• www.drmaribelostrand.com
• www.harrowgate-lisk.com
• They are clean, easy to navigate and calming.
Should not have
• Should not look like a childcare website.

```html
<!DOCTYPE html>
<html lang="en">
<head>
<meta charset="utf-8">
<title>Rosalind Vantreece, LCSW – Stillbrook Wellness</title>
<link href="https://fonts.googleapis.com/css2?family=Bree+Serif&family=Dancing+Script:wght@600&family=Jost:wght@300;400;500;600&family=Lato:wght@400;700&display=swap" rel="stylesheet">
<style>
  :root {
    --sky: #33a6d7;
    --leaf: #9bcb3c;
    --navy: #0355a3;
    --footer: #214f7e;
    --ink: #2b2b2b;
    --body: #4a4a4a;
    --panel: #f1f1f1;
    --rule: #b9b9b9;
    --charcoal: #5e5e5e;
    --brand-text: #d4d4d4;
    --white: #ffffff;
  }
  * { box-sizing: border-box; margin: 0; padding: 0; }
  html, body { width: 1098px; height: 1200px; overflow: hidden; background: var(--white); }
  body { position: relative; font-family: 'Lato', sans-serif; color: var(--body); }

  .hero {
    position: absolute; left: 0; top: 0; width: 1098px; height: 302px;
    background:
      radial-gradient(ellipse 60% 50% at 50% 95%, rgba(196,150,100,.55), transparent 70%),
      linear-gradient(180deg, #6f6358 0%, #4b4a44 35%, #2f3532 70%, #3a342c 100%);
  }
  .hero-phone {
    position: absolute; left: 148px; top: 16px; display: flex; align-items: center; gap: 6px;
    color: var(--white); font-family: 'Lato', sans-serif; font-weight: 700; font-size: 16px;
  }
  .hero-name {
    position: absolute; left: 147px; top: 180px; color: var(--white);
    font-family: 'Bree Serif', serif; font-weight: 400; font-size: 31px; letter-spacing: .5px;
  }
  .hero-title {
    position: absolute; left: 147px; top: 220px; color: var(--white);
    font-family: 'Dancing Script', cursive; font-size: 27px;
  }
  .brand {
    position: absolute; left: 600px; top: 206px; width: 386px; text-align: center;
    color: var(--brand-text); font-family: 'Lato', sans-serif; font-weight: 400;
    font-size: 26px; line-height: 32px;
  }

  .main-nav {
    position: absolute; left: 0; top: 302px; width: 1098px; height: 34px; background: var(--sky);
  }
  .main-nav ul { list-style: none; position: absolute; left: 147px; top: 0; height: 34px; display: flex; }
  .main-nav li {
    height: 34px; display: flex; align-items: center; justify-content: center;
    color: var(--white); font-family: 'Jost', sans-serif; font-size: 14px; letter-spacing: .3px;
    position: relative;
  }
  .main-nav li + li:not(.after-home)::before {
    content: ""; position: absolute; left: 0; top: 6px; height: 22px; width: 1px; background: rgba(255,255,255,.55);
  }
  .main-nav li.active { background: var(--leaf); color: var(--ink); font-weight: 600; }

  .intro { position: absolute; left: 155px; top: 377px; width: 781px; }
  .portrait-frame {
    position: absolute; left: 0; top: 0; width: 218px; height: 258px;
    border: 1px solid var(--rule); padding: 5px; background: var(--white);
  }
  .portrait { width: 100%; height: 100%; background: linear-gradient(160deg, #d9c27a 0%, #c9a95c 45%, #7b8a4a 100%); }
  .intro-text {
    position: absolute; left: 231px; top: 3px; width: 552px;
    font-size: 11.7px; line-height: 18.4px; color: var(--body); letter-spacing: 0;
  }
  .intro-text p + p { margin-top: 10px; }

  .services { position: absolute; left: 0; top: 688px; width: 568px; height: 446px; background: var(--panel); }
  .services-heading {
    position: absolute; left: 150px; top: 22px; font-family: 'Jost', sans-serif; font-weight: 500;
    font-size: 27px; color: var(--ink);
  }
  .services-heading span { color: var(--sky); }
  .services-rule { position: absolute; left: 146px; top: 69px; width: 384px; height: 1px; background: var(--rule); }
  .service { position: absolute; left: 149px; width: 400px; height: 86px; }
  .service-badge {
    position: absolute; left: 0; top: 0; width: 86px; height: 86px; border-radius: 50%;
    border: 1px solid var(--charcoal); padding: 3px; background: var(--white);
  }
  .service-badge i { display: block; width: 100%; height: 100%; border-radius: 50%; background: var(--charcoal); }
  .service-badge.green i { background: var(--leaf); }
  .service-badge.grey { border-color: var(--leaf); }
  .service-name {
    position: absolute; left: 97px; top: 14px; font-family: 'Jost', sans-serif; font-weight: 400;
    font-size: 16px; color: var(--ink); letter-spacing: .2px;
  }
  .service-desc { position: absolute; left: 97px; top: 37px; width: 300px; font-size: 12px; line-height: 18.4px; }

  .signup {
    position: absolute; left: 568px; top: 688px; width: 530px; height: 446px;
    background: linear-gradient(180deg, #5d7fae 0%, #8aa7cb 35%, #a9bed6 55%, #5b7a3c 72%, #3e5a2a 100%);
  }
  .signup-overlay { position: absolute; left: 0; top: 240px; width: 530px; height: 206px; background: rgba(20,30,20,.45); }
  .signup-heading {
    position: absolute; left: 14px; top: 270px; width: 400px; color: var(--white);
    font-family: 'Jost', sans-serif; font-weight: 600; font-size: 17.5px; line-height: 24px; letter-spacing: .3px;
  }
  .signup-input {
    position: absolute; left: 14px; top: 336px; width: 369px; height: 29px; background: var(--white);
    font-size: 12px; color: #333; padding: 6px 6px; line-height: 17px;
  }
  .signup-submit {
    position: absolute; left: 14px; top: 382px; width: 82px; height: 28px; background: var(--leaf);
    color: var(--ink); font-family: 'Jost', sans-serif; font-weight: 600; font-size: 16px; letter-spacing: .6px;
    text-align: center; line-height: 28px;
  }

  .site-footer { position: absolute; left: 0; top: 1134px; width: 1098px; height: 66px; background: var(--footer); color: var(--white); }
  .footer-links { position: absolute; left: 148px; top: 15px; list-style: none; display: flex; font-size: 9.6px; }
  .footer-links li + li::before { content: "|"; margin: 0 7px; }
  .copyright { position: absolute; left: 148px; top: 37px; font-size: 9.6px; }
  .social { position: absolute; left: 846px; top: 15px; display: flex; gap: 7px; }
  .social span { width: 30px; height: 30px; border-radius: 50%; background: var(--white); }
</style>
</head>
<body>
  <header class="hero" role="img" aria-label="Calm water with smooth stepping stones at dusk">
    <div class="hero-phone">
      <svg width="24" height="24" viewBox="0 0 24 24" aria-hidden="true">
        <circle cx="12" cy="12" r="10.5" fill="none" stroke="#fff" stroke-width="1.5"/>
        <path d="M8.3 6.5c.5-.4 1.1-.3 1.4.2l1 1.7c.3.5.1 1-.3 1.3l-.7.5c.5 1.3 1.5 2.4 2.8 3l.5-.7c.3-.4.9-.6 1.3-.3l1.7 1c.5.3.6 1 .2 1.4l-.8.9c-.6.6-1.5.8-2.3.4-2.6-1.2-4.6-3.3-5.7-5.9-.3-.8-.1-1.7.5-2.3z" fill="#fff"/>
      </svg>
      (208)555-7162
    </div>
    <h1 class="hero-name">Rosalind Vantreece</h1>
    <p class="hero-title">LCSW, Registered Play Therapist</p>
    <div class="brand">Stillbrook Wellness</div>
  </header>

  <nav class="main-nav">
    <ul>
      <li class="active" style="width:96px">HOME</li>
      <li class="after-home" style="width:127px">ABOUT ME</li>
      <li style="width:197px">COUNSELING SERVICE</li>
      <li style="width:77px">FEES</li>
      <li style="width:81px">BLOG</li>
      <li style="width:96px">FAQS</li>
      <li style="width:149px">CONTACT ME</li>
    </ul>
  </nav>

  <section class="intro">
    <div class="portrait-frame"><div class="portrait" role="img" aria-label="Portrait of the therapist outdoors in a golden field"></div></div>
    <div class="intro-text">
      <p>Lorem ipsum dolor sit amet, consectetuer adipiscing elit, sed diam nonummy nibh euismod tincidunt ut laoreet dolore magna aliquam erat volutpat. Ut wisi enim ad minim veniam, quis nostrud exerci tation ullamcorper suscipit lobortis nisl ut aliquip ex ea commodo consequat. Duis autem vel eum iriure dolor in hendrerit in vulputate velit esse molestie consequat, vel illum dolore eu feugiat nulla facilisis at vero eros et accumsan et iusto odio dignissim qui blandit praesent luptatum zzril delenit augue duis dolore te feugait nulla facilisi.Lorem ipsum dolor sit amet, consectetuer adipiscing elit, sed diam nonummy nibh euismod tincidunt ut laoreet dolore magna aliquam erat volutpat. Ut wisi enim ad minim veniam, quis nostrud exerci tation ullamcorper suscipit lobortis nisl ut aliquip ex ea commodo consequat. Duis autem vel eum iriure dolor in hendrerit in vulputate velit esse molestie consequat,</p>
      <p>Lorem ipsum dolor sit amet, consectetuer adipiscing elit, sed diam nonummy nibh euismod tincidunt ut laoreet dolore magna aliquam erat volutpat. Ut wisi enim ad minim veniam, quis nostrud exerci tation ullamcorper suscipit lobortis nisl ut aliquip ex ea commodo consequat. Duis autem vel eum iriure dolor in hendrerit in vulputate velit esse molestie consequat.</p>
    </div>
  </section>

  <section class="services">
    <h2 class="services-heading">Counseling <span>Services</span></h2>
    <div class="services-rule"></div>
    <div class="service" style="top:99px">
      <div class="service-badge green" role="img" aria-label="Individual counseling icon"><i></i></div>
      <h3 class="service-name">INDIVIDUAL COUNSELING</h3>
      <p class="service-desc">Lorem ipsum dolor sit amet, consectetuer adipiscing elit sed diam nonummy nibh euismod tincidunt ut.</p>
    </div>
    <div class="service" style="top:217px">
      <div class="service-badge grey" role="img" aria-label="Play therapy icon"><i></i></div>
      <h3 class="service-name">PLAY THERAPY</h3>
      <p class="service-desc">Lorem ipsum dolor sit amet, consectetuer adipiscing elit sed diam nonummy nibh euismod tincidunt ut.</p>
    </div>
    <div class="service" style="top:326px">
      <div class="service-badge grey" role="img" aria-label="Sandplay therapy icon"><i></i></div>
      <h3 class="service-name">SANDPLAY THERAPY</h3>
      <p class="service-desc">Lorem ipsum dolor sit amet, consectetuer adipiscing elit sed diam nonummy nibh euismod tincidunt ut.</p>
    </div>
  </section>

  <section class="signup" role="img" aria-label="Woman raising her arms joyfully in a grassy meadow under a blue sky">
    <div class="signup-overlay"></div>
    <h2 class="signup-heading">Sign Up With Your Email Address To Receive News And Updates!</h2>
    <div class="signup-input">Email Address</div>
    <div class="signup-submit">SUBMIT</div>
  </section>

  <footer class="site-footer">
    <ul class="footer-links">
      <li>Home</li><li>About Me</li><li>Counseling Service</li><li>Fees</li><li>Blog</li><li>Faqs</li><li>Contact Me</li>
    </ul>
    <p class="copyright">Copyright © 2016 Stillbrook Wellness.&nbsp; All Rights Reserved</p>
    <div class="social" aria-label="Social media links">
      <span role="img" aria-label="Social link one"></span>
      <span role="img" aria-label="Social link two"></span>
      <span role="img" aria-label="Social link three"></span>
    </div>
  </footer>
</body>
</html>
```